依頼詳細
ラフ案を添付致しますのでそちらをベースにブラッシュアップお願いいたします。

お水の特徴は以下となります。
①分子が細かい(水分子のナノコロイダル化、六角形構造)
②浸透力が高い(脳細胞まで届くイメージ)
③科学的に研究された機能のある水

全体デザインは、上記イメージを踏まえてエネルギー溢れるようなデザインを希望致します。
記載項目
下部に記載する社名等はデザイン選定後にお伝えさせていただきます。
サイズ
A4
ページ数
片面
希望イメージ
シンプル 複雑
単色 カラフル
暗い 明るい
日常 高級
遊び心 厳粛
未来的 伝統的
女性的 男性的
希望する色
水色系
納品ファイル
• 高解像度JPG (.jpg)
• イラストレーター形式 (.ai)
• PNG形式 (.png)
補足説明
■ 選んだ理由

インパクトと躍動感のあるデザインだった為選ばせて頂きました。

■ 提案者全員のお礼・コメント

この度はたくさんのご提案誠にありがとうございます。
素敵なデザインが多く選定に悩ませて頂きました。
また機会がありましたらその際はどうぞよろしくお願い致します。

```html
<!DOCTYPE html>
<html lang="ja">
<head>
<meta charset="UTF-8">
<title>高濃度シリカ水 OEM</title>
<link href="https://fonts.googleapis.com/css2?family=Noto+Sans+JP:wght@400;500;700;900&display=swap" rel="stylesheet">
<style>
  :root{
    --navy:#13356b;
    --blue:#1d6fc4;
    --sky:#4aa9e6;
    --pale:#e6f3fc;
    --ice:#f4faff;
    --gold:#b89244;
    --white:#ffffff;
    --text:#1f2b3d;
  }
  *{box-sizing:border-box;margin:0;padding:0}
  html,body{width:846px;height:1200px;overflow:hidden;background:var(--white)}
  body{font-family:"Noto Sans JP",sans-serif;color:var(--text)}
  .flyer{position:relative;width:846px;height:1200px;background:linear-gradient(180deg,#fff 0%,#fff 60%,var(--ice) 100%)}

  .lead{position:absolute;top:26px;left:0;width:100%;text-align:center;font-weight:900;font-size:33px;line-height:1.3;color:var(--navy);white-space:nowrap}
  .lead em{font-style:normal;color:var(--blue)}
  .lead .mark{border-bottom:4px solid var(--sky)}

  .hero{position:absolute;top:92px;left:0;width:846px;height:480px;
    background:radial-gradient(ellipse at 25% 60%,#e9f6ff 0%,#9fd3f4 35%,#3d95d8 70%,#1a5fae 100%)}
  .hero-title{position:absolute;top:24px;left:120px;display:flex;align-items:flex-end;gap:14px}
  .hero-title h1{background:rgba(255,255,255,.92);color:var(--blue);font-weight:900;font-size:62px;line-height:1;padding:10px 18px 14px;letter-spacing:2px;white-space:nowrap}
  .lot{background:var(--white);border:2px solid var(--blue);color:var(--navy);font-weight:700;font-size:20px;line-height:1.25;padding:6px 12px;margin-bottom:6px;white-space:nowrap;text-align:center}
  .features{position:absolute;top:130px;left:475px;display:grid;grid-template-columns:162px 162px;gap:14px 20px}
  .feature{width:162px;height:162px;border-radius:50%;background:rgba(255,255,255,.9);border:3px solid var(--blue);display:flex;align-items:center;justify-content:center;text-align:center;color:var(--navy);font-weight:900;font-size:22px;line-height:1.3}
  .feature small{display:block;font-size:13px;font-weight:700;color:var(--blue);white-space:nowrap}
  .feature.dark{background:var(--blue);color:var(--white);border-color:var(--white)}
  .feature.dark small{color:#d9efff}

  .statement{position:absolute;top:590px;left:60px;width:726px;padding:16px 0;border-top:2px solid var(--gold);border-bottom:2px solid var(--gold);text-align:center;font-size:19px;font-weight:700;line-height:1.75;color:var(--navy);white-space:nowrap}
  .statement strong{color:var(--blue);font-weight:900;font-size:23px}

  .compare{position:absolute;top:720px;left:30px;width:786px;height:400px;background:var(--pale)}
  .compare-head{display:grid;grid-template-columns:1fr 1fr;background:linear-gradient(90deg,var(--blue),var(--sky));color:var(--white);text-align:center;height:96px;align-items:center}
  .compare-head p{font-size:21px;font-weight:700;line-height:1.3}
  .compare-head p b{display:block;font-size:30px;font-weight:900}
  .cross{position:absolute;left:373px;top:18px;font-size:54px;font-weight:400;line-height:1;padding-top:6px;color:var(--white)}
  .compare-body{display:grid;grid-template-columns:1fr 1fr;gap:20px;padding:20px}
  .points{background:var(--white);padding:20px 18px;list-style:none;height:264px}
  .points li{position:relative;padding-left:30px;font-size:18px;font-weight:500;line-height:1.5;margin-bottom:16px}
  .points li::before{content:"";position:absolute;left:0;top:5px;width:18px;height:18px;border:2px solid var(--blue);background:var(--pale)}
  .science{background:var(--white);padding:14px;height:264px;text-align:center}
  .molecules{height:136px;border-radius:6px;background:radial-gradient(circle at 28% 50%,#cfe6f8 0%,#eef7fd 40%,transparent 42%),radial-gradient(circle at 72% 50%,#bfe3fb 0%,#e8f5ff 40%,transparent 42%),var(--ice)}
  .labels{display:flex;justify-content:space-around;font-size:15px;font-weight:700;color:var(--navy);margin:6px 0 8px;white-space:nowrap}
  .science .note{font-size:19px;font-weight:900;color:var(--navy);border-bottom:2px solid var(--sky);display:inline-block;padding:0 8px}
  .science .result{margin-top:6px;font-size:25px;font-weight:900;color:var(--blue)}
</style>
</head>
<body>
<main class="flyer">
  <p class="lead">話題の<em class="mark">シリカ水</em>を<em class="mark">自社ブランド</em>でつくりませんか？</p>

  <section class="hero" role="img" aria-label="水しぶきに囲まれたシリカ水のペットボトル（500mlと2L）">
    <div class="hero-title">
      <h1>高濃度シリカ水</h1>
      <div class="lot">小ロット<br>100本〜</div>
    </div>
    <div class="features">
      <div class="feature">シリカ濃度<br>調整可</div>
      <div class="feature dark"><span>非晶質シリカ<small>「水溶性ケイ素aqlu」</small>配合</span></div>
      <div class="feature dark"><span>選べる<br>サイズ<small>500ml・2L</small></span></div>
      <div class="feature">科学的に<br>優れた<br>機能水</div>
    </div>
  </section>

  <p class="statement">注目のミネラル「シリカ」とカラダに浸透しやすい機能水をブレンドし<br>独自技術によって<strong>ナノコロイダル化</strong>に成功した<strong>高濃度シリカ水</strong></p>

  <section class="compare">
    <div class="compare-head">
      <p>非晶質シリカ<b>水溶性ケイ素aqlu</b></p>
      <p>科学的に優れた水<b>機能水</b></p>
    </div>
    <span class="cross">×</span>
    <div class="compare-body">
      <ul class="points">
        <li>機能性、安全性エビデンスの充実（ヒト臨床試験済、非晶質データ）</li>
        <li>アジアハラール認証取得</li>
        <li>シリカは鉱物由来、植物由来の２種タイプから選択可能</li>
      </ul>
      <div class="science">
        <div class="molecules" role="img" aria-label="一般的な水の大きな分子と生体機能水の小さな分子の比較図"></div>
        <div class="labels"><span>一般的な水（分子大）</span><span>生体機能水（分子小）</span></div>
        <p class="note">微細分子＆活発な状態</p>
        <p class="result">⇒浸透性が高い</p>
      </div>
    </div>
  </section>
</main>
</body>
</html>
```